Latin Concert Series in Miami Flyer

We are hosting an 8 week concert series in Miami, which will take place on the water with a beautiful background view at Miami's busiest venue. We need to take the attached file which contains information and photos, and lay it out in a very visually compelling way that is unique and creative.

Target Market(s)

Miami, Latin, Hispanic, Music

Industry/Entity Type

Advertising

Font styles to use
Other font styles liked:
• Calibri Light is a great font

Colors

Designer to choose colors to be used in the design.

Requirements
Must have
• Creativity, heavy on visuals. Here is a FileCrate Link containing some great visuals: https://www.filecrate-share.com/sh/k2m9tq4wz7/visuals?dl=0
• Brightwave Studio Logo:
• https://www.filecrate-share.com/s/p4r8vn1jd3/Logo%20Highres%20With%20%20text.jpg?dl=0
Nice to have
• Great visual design, soft on eyes, playful because this is a concert series in Miami on the water during the holidays.
Should not have
• Boxy, corporate fonts. This needs to be soft on eyes, light colors.

```html
<!DOCTYPE html>
<html lang="en">
<head>
<meta charset="utf-8">
<title>Prime Sponsorship Opportunity – Brightwave Studio</title>
<link href="https://fonts.googleapis.com/css2?family=Carlito:wght@400;700&family=Open+Sans:wght@600;700&family=Oswald:wght@500&display=swap" rel="stylesheet">
<style>
  :root {
    --page-bg: #e9e9ea;
    --sheet: #f3f3f3;
    --teal: #2a8a8f;
    --teal-light: #5fcfc3;
    --magenta: #b51e6a;
    --pink: #e0197c;
    --ink: #4a4a4a;
    --ink-dark: #2b2b2b;
  }
  * { box-sizing: border-box; margin: 0; padding: 0; }
  html, body { width: 1200px; height: 1200px; overflow: hidden; background: var(--page-bg); }
  body { position: relative; font-family: "Carlito", "Calibri", sans-serif; }

  .flyer {
    position: absolute; left: 376px; top: 20px;
    width: 447px; height: 1160px;
    background: linear-gradient(180deg, #f6f6f6, #ececec);
    overflow: hidden;
    box-shadow: 0 6px 24px rgba(0,0,0,.18);
  }
  .hero { position: absolute; left: 0; top: 0; width: 447px; height: 250px; }

  .brand-badge {
    position: absolute; left: 298px; top: 131px;
    width: 104px; height: 104px; border-radius: 50%;
    background: #fff; box-shadow: 0 2px 6px rgba(0,0,0,.2);
    display: flex; align-items: center; justify-content: center; text-align: center;
    font-family: "Carlito", sans-serif; font-weight: 700; font-size: 13px; line-height: 1.1;
    color: var(--ink-dark); letter-spacing: .5px;
  }

  .headline { position: absolute; left: 0; width: 100%; text-align: center; color: var(--teal); font-family: "Open Sans", sans-serif; font-weight: 700; }
  .headline--small { top: 248px; font-size: 27px; }
  .headline--large { top: 274px; font-size: 46px; letter-spacing: .5px; }

  .copy { position: absolute; left: 30px; right: 30px; text-align: center; color: var(--ink); font-size: 10.5px; line-height: 1.2; }
  .copy--intro { top: 329px; }
  .copy--invite { top: 395px; }

  .dates {
    position: absolute; top: 352px; left: 0; width: 100%; text-align: center;
    font-family: "Oswald", sans-serif; font-weight: 500; font-size: 33px; color: var(--magenta);
    letter-spacing: .3px;
  }
  .site-link {
    position: absolute; top: 421px; left: 0; width: 100%; text-align: center;
    font-size: 14px; color: var(--ink-dark); text-decoration: underline; letter-spacing: .4px;
  }

  .pill {
    position: absolute; left: 50%; transform: translateX(-50%);
    background: var(--teal-light); border-radius: 28px;
    display: flex; align-items: center; justify-content: center; text-align: center;
    color: #1f3b3c; font-size: 10.5px; line-height: 1.3; letter-spacing: .3px;
    box-shadow: 0 2px 4px rgba(0,0,0,.18);
  }
  .pill--signage { top: 443px; width: 211px; height: 54px; padding: 0 18px; }
  .pill--activation { top: 629px; width: 211px; height: 52px; font-size: 12px; }

  .photo-row { position: absolute; left: 13px; width: 421px; display: flex; justify-content: space-between; }
  .photo-row--signage { top: 508px; }
  .photo-row--activation { top: 700px; }
  .photo { width: 133px; height: 103px; }
  .photo--building { background: linear-gradient(160deg, #9c7a5e, #c46448 55%, #5a4a3c); }
  .photo--banner { background: linear-gradient(180deg, #c8443f, #e7e1db 60%, #8a8580); }
  .photo--garage { background: linear-gradient(180deg, #6e6a64, #c9443d 50%, #4c4a47); }
  .photo--tents { background: linear-gradient(180deg, #7da05c, #d04444 50%, #b9a58c); }
  .photo--crowd { background: linear-gradient(180deg, #3f8fd2, #86b0c6 45%, #5b6f7a); }
  .photo--studio { background: linear-gradient(180deg, #1f2c44, #3b5f9a 60%, #2c6fbe); }

  .sponsor-row {
    position: absolute; left: 20px; right: 20px;
    display: flex; justify-content: center; align-items: center; gap: 14px;
    color: var(--ink-dark); font-size: 9px; font-weight: 700; white-space: nowrap;
  }
  .sponsor-row--1 { top: 837px; }
  .sponsor-row--2 { top: 869px; }
  .sponsor-row--3 { top: 901px; font-size: 7.5px; }
  .sponsor-row--4 { top: 936px; font-size: 6.5px; gap: 12px; }
  .sponsor { display: inline-flex; align-items: center; gap: 3px; }
  .sponsor .mark { width: 8px; height: 8px; background: var(--ink-dark); }
  .partner-seal { width: 10px; height: 10px; border-radius: 50%; background: #9a9a9a; }

  .footer-art { position: absolute; left: 0; top: 975px; width: 447px; height: 185px; }
</style>
</head>
<body>
  <main class="flyer">
    <svg class="hero" viewBox="0 0 447 250" aria-hidden="false">
      <defs>
        <linearGradient id="bay" x1="0" y1="0" x2="1" y2="1">
          <stop offset="0" stop-color="#2f7fbf"/>
          <stop offset=".45" stop-color="#6f8fa0"/>
          <stop offset=".75" stop-color="#4f8a5a"/>
          <stop offset="1" stop-color="#8aa8b8"/>
        </linearGradient>
      </defs>
      <rect width="447" height="250" fill="url(#bay)" role="img" aria-label="Aerial view of the Miami waterfront skyline, marina and arena"/>
      <path d="M0 205 C110 250 250 235 330 185 C380 155 420 148 447 145 L447 250 L0 250 Z" fill="var(--pink)"/>
      <path d="M0 212 C110 256 250 244 330 196 C380 166 420 160 447 158 L447 250 L0 250 Z" fill="#f6f6f6"/>
    </svg>
    <div class="brand-badge">Brightwave<br>Studio</div>

    <h1 class="headline headline--small">PRIME SPONSORSHIP</h1>
    <h2 class="headline headline--large">OPPORTUNITY</h2>
    <p class="copy copy--intro">From the producers of Brightwave Festival comes an eight week concert series at Miami's most trafficked venue, Harborview Marketplace.</p>
    <p class="dates">DECEMBER 2017- JANUARY 2018</p>
    <p class="copy copy--invite">Become a sponsor of this amazing concert series celebrating up and coming latino artists on the Rising Voices Track (RVT) stage</p>
    <p class="site-link">WWW.BRIGHTWAVESTUDIO-EVENTS.COM</p>

    <div class="pill pill--signage">ACTIVATE YOUR BRAND ONSITE AT HARBORVIEW MARKETPLACE WITH HIGH IMPACT SIGNAGE</div>
    <div class="photo-row photo-row--signage">
      <div class="photo photo--building" role="img" aria-label="Festival banner on the marketplace building at sunset"></div>
      <div class="photo photo--banner" role="img" aria-label="Festival backdrop banner at an indoor event"></div>
      <div class="photo photo--garage" role="img" aria-label="Festival signage in a parking garage"></div>
    </div>

    <div class="pill pill--activation">BRAND ACTIVATION ONSITE</div>
    <div class="photo-row photo-row--activation">
      <div class="photo photo--tents" role="img" aria-label="Sponsor tents with visitors at an outdoor activation"></div>
      <div class="photo photo--crowd" role="img" aria-label="Crowd gathered at the waterfront marketplace"></div>
      <div class="photo photo--studio" role="img" aria-label="Live television broadcast set at the venue"></div>
    </div>

    <div class="sponsor-row sponsor-row--1">
      <span class="sponsor"><span class="mark"></span>Ridewell</span>
      <span class="sponsor">Connexa</span>
      <span class="sponsor">Platehop</span>
      <span class="sponsor">Dolcera</span>
      <span class="sponsor">Snapbite</span>
      <span class="sponsor">Lumo</span>
    </div>
    <div class="sponsor-row sponsor-row--2">
      <span class="sponsor">Pedalhaus</span>
      <span class="sponsor">Coral Rum</span>
      <span class="sponsor">Frostfizz</span>
      <span class="sponsor">Stonebeat</span>
      <span class="sponsor"><span class="mark"></span>Tallybox</span>
      <span class="sponsor">Aerolis</span>
    </div>
    <div class="sponsor-row sponsor-row--3">
      <span class="sponsor">Canal Sol 51</span>
      <span class="sponsor">Vista 6</span>
      <span class="sponsor">Bay Courier</span>
      <span class="sponsor">Roving Mo</span>
      <span class="sponsor">Tidecast</span>
      <span class="sponsor">Sunmark</span>
    </div>
    <div class="sponsor-row sponsor-row--4">
      <span class="sponsor">Ashby Holdings</span>
      <span class="sponsor">Civic Arts</span>
      <span class="sponsor">Palmcrest College</span>
      <span class="sponsor">Bay Guild</span>
      <span class="sponsor">Gulfview University</span>
      <span class="partner-seal"></span>
      <span class="partner-seal"></span>
      <span class="partner-seal"></span>
    </div>

    <svg class="footer-art" viewBox="0 0 447 185">
      <defs>
        <linearGradient id="stage" x1="0" y1="0" x2="1" y2="1">
          <stop offset="0" stop-color="#7a2a9a"/>
          <stop offset=".5" stop-color="#d0309a"/>
          <stop offset="1" stop-color="#5a2a8a"/>
        </linearGradient>
        <linearGradient id="spot" x1="0" y1="0" x2="0" y2="1">
          <stop offset="0" stop-color="#c9b6d6"/>
          <stop offset="1" stop-color="#6a3a8a"/>
        </linearGradient>
      </defs>
      <path d="M0 62 C70 20 170 15 260 50 C300 65 330 70 447 60 L447 185 L0 185 Z" fill="var(--teal-light)"/>
      <path d="M0 72 C70 32 170 27 260 62 C300 77 330 82 447 72 L447 185 L0 185 Z" fill="url(#stage)" role="img" aria-label="Rappers performing on a stage with magenta lights"/>
      <circle cx="362" cy="74" r="86" fill="var(--teal-light)"/>
      <circle cx="362" cy="74" r="79" fill="url(#spot)" role="img" aria-label="Singer performing with dancers on stage"/>
    </svg>
  </main>
</body>
</html>
```